Flyer-Design für Immobilienunternehmen
Zielgruppe
Verkauf von Immobilien und Grundstücken, Immobilienbewertung, Netzwerken in der Immobilienbranche
Private und gewerbliche Immobilien- und Grundstücksbesitzer, Erbengemeinschaften
Aufgabenstellung
Immobilienfachwirtin, Unternehmerin, Erfahrung,
Ich nehme mir Zeit für den Kunden

```html
<!DOCTYPE html>
<html lang="de">
<head>
<meta charset="utf-8">
<title>Lindner Immobilien – Flyer</title>
<link href="https://fonts.googleapis.com/css2?family=Montserrat:wght@400;500;600;700&family=Raleway:wght@400;500;600&display=swap" rel="stylesheet">
<style>
:root{
  --green-dark:#5f9a3e;
  --green:#7cb342;
  --green-light:#a6cf4a;
  --mint:#eaf3dc;
  --ink:#333;
  --grey:#555;
  --bg:#e6e6e6;
  --white:#fff;
}
*{box-sizing:border-box;margin:0;padding:0}
html,body{width:1200px;height:2400px;overflow:hidden;background:var(--bg);font-family:"Montserrat",sans-serif;color:var(--ink)}
.sheet{position:absolute;left:90px;width:1020px;display:flex;box-shadow:0 4px 14px rgba(0,0,0,.15)}
.sheet--outside{top:120px;height:1000px}
.sheet--inside{top:1320px;height:1050px}
.panel{position:relative;width:340px;height:100%;background:var(--white);overflow:hidden}
.panel--green{background:linear-gradient(135deg,var(--green-dark) 0%,var(--green) 55%,var(--green-light) 100%);color:var(--white)}
.photo{position:absolute;left:0;width:100%}
.photo--office{background:linear-gradient(160deg,#c9ccc6,#8e9a84 60%,#5c6a50)}
.photo--portrait{background:linear-gradient(180deg,#eaf3dc,#d5c2a8 55%,#2b2b2b)}
.photo--pastel{background:linear-gradient(180deg,#9cc55a,#d8b8a2 55%,#6a6a5a)}
.heading{font-family:"Raleway",sans-serif;font-weight:500;letter-spacing:.5px;text-transform:uppercase}
.rule-title{display:flex;align-items:center;gap:8px;padding:0 0 0 0;color:var(--green-dark);font-family:"Raleway",sans-serif;font-weight:500;font-size:16px;text-transform:uppercase}
.rule-title::before,.rule-title::after{content:"";flex:1;height:1.5px;background:var(--green)}
.body{font-size:10.5px;line-height:1.45;color:var(--grey);margin-bottom:10px}
.lead{font-size:11.5px;font-weight:600;color:var(--ink);margin:14px 0 10px}
.band{background:linear-gradient(90deg,var(--green-dark),var(--green-light));color:var(--white);text-align:center;font-size:11px;line-height:1.35;padding:10px 18px}
.brand{font-family:"Montserrat",sans-serif;font-weight:600;color:var(--green-dark);text-align:center;text-transform:uppercase;letter-spacing:2px}
.brand__name{font-size:34px;line-height:1}
.brand__sub{font-size:13px;letter-spacing:3px;margin-top:4px}
.brand__dot{width:46px;height:46px;border-radius:50%;background:var(--green);margin:0 auto 12px}
.web{font-size:15px;font-weight:500;text-align:center;letter-spacing:.5px;color:var(--ink)}
.icon{display:block;margin:0 auto}
.section{padding:0 22px 0 22px}
</style>
</head>
<body>

<!-- Outside spread -->
<div class="sheet sheet--outside">

  <section class="panel panel--intro">
    <div class="photo photo--office" style="top:0;height:260px" role="img" aria-label="Foto: Maklerin am Schreibtisch im Büro"></div>
    <div style="position:absolute;top:282px;left:0;right:0">
      <h2 class="rule-title" style="font-size:20px;color:var(--ink)">Immobilienverkauf</h2>
    </div>
    <div class="section" style="position:absolute;top:340px;left:0;right:0">
      <p class="body">Eine Immobilie zu verkaufen, ob die eigene oder eine geerbte, geht nicht von heute auf morgen. Ich verstehe mich als Partnerin an Ihrer Seite, die lösungsorientiert zuhört und Sie im ganzen Prozess begleitet.</p>
      <p class="body">Der Verkauf Ihrer Immobilie ist für mich nicht nur die Bewertung, das Exposé und die Verhandlungen nach der Besichtigung. Mein Ziel ist es, gemeinsam mit Ihnen alle Aspekte zu beleuchten. Dafür braucht es Zeit und aktuelles Fachwissen.</p>
      <p class="body">Meine strukturierte Herangehensweise macht den Prozess für Sie transparent. In jeder Phase nehme ich mir die nötige Zeit, damit Sie danach sagen können: es passt.</p>
    </div>
    <div class="band" style="position:absolute;top:660px;left:0;right:0;height:80px;font-size:14px;font-weight:500;text-align:left;padding:16px 22px">Mit Hilfe von Marlene Lindner habe ich den Käufer gefunden, der passt.</div>
    <div class="photo photo--office" style="top:740px;height:260px" role="img" aria-label="Foto: Maklerin beim Ausfüllen von Unterlagen"></div>
  </section>

  <section class="panel">
    <div class="panel--green" style="position:absolute;top:0;left:0;right:0;height:760px">
      <h1 class="heading" style="position:absolute;top:400px;left:0;right:0;text-align:center;font-size:27px;line-height:1.25">Ich nehme mir<br>Zeit für Sie!</h1>
      <div style="position:absolute;top:505px;left:30px;right:30px;height:180px;border:1.5px solid rgba(255,255,255,.8);padding:0 20px">
        <p style="text-align:center;font-size:14px;line-height:1.3;margin-top:-9px;background:transparent"><span style="background:linear-gradient(90deg,#6ea640,#78b043);padding:0 6px">Vereinbaren Sie einen</span><br>unverbindlichen persönlichen Gesprächstermin mit mir:</p>
        <div style="height:1px;background:rgba(255,255,255,.7);margin:12px 30px 20px"></div>
        <p style="display:flex;align-items:center;gap:12px;font-size:13px;margin-bottom:18px">
          <svg width="20" height="20" viewBox="0 0 24 24"><path d="M6.6 10.8c1.4 2.8 3.8 5.1 6.6 6.6l2.2-2.2c.3-.3.7-.4 1-.2 1.1.4 2.3.6 3.6.6.6 0 1 .4 1 1V20c0 .6-.4 1-1 1C10.6 21 3 13.4 3 4c0-.6.4-1 1-1h3.5c.6 0 1 .4 1 1 0 1.3.2 2.5.6 3.6.1.3 0 .7-.2 1z" fill="#fff"/></svg>
          04321/55 67 890</p>
        <p style="display:flex;align-items:center;gap:12px;font-size:13px">
          <svg width="20" height="16" viewBox="0 0 20 16"><rect x="1" y="1" width="18" height="14" fill="none" stroke="#fff" stroke-width="1.6"/><path d="M1 1l9 8 9-8" fill="none" stroke="#fff" stroke-width="1.6"/></svg>
          info@lindner-immobilien</p>
      </div>
    </div>
    <div style="position:absolute;top:800px;left:0;right:0">
      <div class="brand__dot"></div>
      <div class="brand"><div class="brand__name">Lindner</div><div class="brand__sub">Immobilien</div></div>
      <p class="web" style="margin-top:26px">WWW.LINDNER.IMMOBILIEN</p>
    </div>
  </section>

  <section class="panel">
    <div style="position:absolute;top:34px;left:0;right:0">
      <div class="brand__dot"></div>
      <div class="brand"><div class="brand__name">Lindner</div><div class="brand__sub">Immobilien</div></div>
    </div>
    <div style="position:absolute;top:200px;left:0;right:0;height:6px;background:var(--green-light)"></div>
    <div class="photo photo--portrait" style="top:206px;height:540px" role="img" aria-label="Porträtfoto der Maklerin am Tisch"></div>
    <svg style="position:absolute;top:460px;left:0" width="340" height="300" viewBox="0 0 340 300"><path d="M0 280 C150 300 300 200 340 60 L340 90 C300 230 150 300 0 300 Z" fill="var(--green)"/></svg>
    <h2 class="heading" style="position:absolute;top:770px;left:18px;font-size:22px;color:var(--ink)">Immobilienverkauf</h2>
    <div class="band heading" style="position:absolute;top:815px;left:0;right:0;height:100px;font-size:24px;line-height:1.2;padding-top:20px">Ich nehme mir<br>Zeit für Sie!</div>
    <p class="web" style="position:absolute;top:940px;left:0;right:0">WWW.LINDNER.IMMOBILIEN</p>
    <div style="position:absolute;bottom:0;left:0;right:0;height:6px;background:var(--green-light)"></div>
  </section>
</div>

<!-- Inside spread -->
<div class="sheet sheet--inside">

  <section class="panel">
    <div style="position:absolute;top:30px;left:0;right:0">
      <svg class="icon" width="26" height="30" viewBox="0 0 26 30"><circle cx="13" cy="12" r="8" fill="none" stroke="var(--green)" stroke-width="2"/><rect x="9" y="21" width="8" height="5" fill="var(--green)"/></svg>
      <h3 class="rule-title" style="margin-top:6px">1) Sich klar werden</h3>
      <div class="section">
        <p class="lead">Die eigene Verkaufsbereitschaft auf den Prüfstand stellen</p>
        <p class="body">Neben der Klärung der Eigentumsverhältnisse, z.B. bei einer Erbengemeinschaft, geht es um Ihre Motivation und Verkaufsbereitschaft.</p>
        <p class="body">Haben Sie alle Möglichkeiten wie Renovierung und Vermietung durchdacht und eine Rentabilität berechnet? Ist ein Verkauf die richtige Entscheidung?</p>
      </div>
      <div class="band">Ich stelle Ihnen die passenden Fragen,<br>damit Sie sich klarwerden können.</div>
    </div>
    <div style="position:absolute;top:370px;left:0;right:0">
      <svg class="icon" width="26" height="30" viewBox="0 0 26 30"><rect x="4" y="3" width="18" height="24" fill="none" stroke="var(--green)" stroke-width="2"/><path d="M8 10h10M8 15h10M8 20h6" stroke="var(--green)" stroke-width="2"/></svg>
      <h3 class="rule-title" style="margin-top:6px">2) Maklerauftrag</h3>
      <div class="section">
        <p class="lead">Ihre Ziele entscheiden über die Art des Auftrags</p>
        <p class="body">Grundsätzlich können Sie sich entscheiden, ob Sie mich als Alleinmaklerin oder Nachweis- und Vermittlungsmaklerin beauftragen.</p>
        <p class="body">Ihr Vorteil bei der Alleinvermarktung ist, dass ich im festgelegten Zeitraum nachweisbar für Ihren Immobilienverkauf tätig werden muss.</p>
      </div>
      <div class="band">Die Transparenz durch die<br>Nachweisbarkeit gibt Ihnen Sicherheit.</div>
    </div>
    <div style="position:absolute;top:700px;left:0;right:0">
      <svg class="icon" width="28" height="28" viewBox="0 0 24 24"><path d="M12 2l3 7h7l-5.5 4.5 2 7.5L12 16.5 5.5 21l2-7.5L2 9h7z" fill="var(--green)"/></svg>
      <h3 class="rule-title" style="margin-top:6px">3) Immobilienbewertung</h3>
      <div class="section">
        <p class="lead">Sich Zeit nehmen für Details</p>
        <p class="body">Basis für eine erfolgreiche Präsentation ist die Bewertung Ihrer Immobilie. Für diese nehme ich mir viel Zeit.</p>
        <p class="body">Neben einer Markteinschätzung fließen die baulichen Aspekte und die rechtlichen Gegebenheiten wie der Grundbuchauszug, die Bebauungsmöglichkeiten, die Vorgaben der Gemeinde und das Umfeld der Immobilie mit ein.</p>
      </div>
      <div class="band">Gemeinsam arbeiten wir die Details für eine<br>erfolgreiche Verkaufs- &amp; Präsentationsstrategie aus.</div>
    </div>
  </section>

  <section class="panel panel--green">
    <div style="position:absolute;top:30px;left:0;right:0;padding:0 26px">
      <svg class="icon" width="30" height="30" viewBox="0 0 30 30"><circle cx="15" cy="15" r="12" fill="none" stroke="#fff" stroke-width="2"/><path d="M8 17l7-6 7 6" fill="none" stroke="#fff" stroke-width="2"/></svg>
      <h3 class="rule-title" style="color:#fff;margin:6px -26px 0;font-size:14px"><span>Zeit für Transparenz</span></h3>
      <p style="font-size:11px;font-weight:600;margin-top:30px">WIE SCHAFFT MAN TRANSPARENZ?</p>
      <p style="font-size:10.5px;font-weight:500;margin-top:12px;line-height:1.4">Aus meiner Sicht, indem man zuhört und vermittelt. Und das in jeder Phase des Immobilienverkaufs.</p>
      <div style="width:38px;height:1px;background:#fff;margin:14px 0"></div>
      <p style="font-size:10.5px;font-weight:500;line-height:1.4">Für mich gibt es 6 wesentliche Schritte um das bestmögliche Verkaufsergebnis für Sie zu erreichen:</p>
      <ol style="list-style:none;margin-top:22px;font-size:10.5px;font-weight:500">
        <li style="margin-bottom:17px">1) &nbsp;Sich klarwerden</li>
        <li style="margin-bottom:17px">2) &nbsp;Richtige Art des Maklerauftrags festlegen</li>
        <li style="margin-bottom:17px">3) &nbsp;Immobilienbewertung mit Detailbetrachtung</li>
        <li style="margin-bottom:17px">4) &nbsp;Optimale Präsentation- und Verkaufsstrategie</li>
        <li style="margin-bottom:17px">5) &nbsp;Besichtigung – den passenden Käufer finden</li>
        <li style="margin-bottom:17px">6) &nbsp;Kaufvertrag aushandeln – Übergabe begleiten</li>
      </ol>
      <p style="font-size:10.5px;font-weight:500;margin-top:14px;line-height:1.4">Nehmen Sie sich die Zeit, diese Schritte gemeinsam mit mir „ZU DENKEN“.</p>
      <p class="heading" style="text-align:center;font-size:14px;margin-top:28px;line-height:1.4">Der Prozess Ihres Verkaufs wird<br>so für Sie transparenter.</p>
    </div>
    <div class="photo photo--pastel" style="top:740px;bottom:0;left:60px;width:280px;border-radius:140px 140px 0 0" role="img" aria-label="Porträtfoto der Maklerin in geblümter Bluse"></div>
  </section>

  <section class="panel">
    <div style="position:absolute;top:30px;left:0;right:0">
      <svg class="icon" width="28" height="28" viewBox="0 0 28 28"><rect x="3" y="3" width="22" height="16" fill="none" stroke="var(--green)" stroke-width="2"/><path d="M7 15l5-5 4 3 5-6M14 19v5M9 25h10" fill="none" stroke="var(--green)" stroke-width="2"/></svg>
      <h3 class="rule-title" style="margin-top:6px;text-align:center">4) Präsentation- und<br>Verkaufsstrategie</h3>
      <div class="section">
        <p class="lead">Den potentiellen Käufer optimal ansprechen</p>
        <p class="body">Entsprechend der Zielgruppe für Ihre Immobilie erarbeite ich die Präsentations- und Verkaufsstrategie auf Basis der Bewertung. Ein Eintrag in den bekannten Portalen reicht nicht immer. Ein ansprechendes Exposé, passende Außenwerbung oder auch Diskretion, wenn es notwendig ist, fließt in die Strategie mit ein.</p>
      </div>
      <div class="band">Die Bedürfnisse der potentiellen Käufer erkennen und Ihre Immobilien entsprechend präsentieren, ist der Schlüssel zum Verkaufserfolg.</div>
    </div>
    <div style="position:absolute;top:390px;left:0;right:0">
      <svg class="icon" width="28" height="28" viewBox="0 0 28 28"><circle cx="16" cy="11" r="8" fill="none" stroke="var(--green)" stroke-width="2"/><circle cx="16" cy="11" r="3" fill="var(--green)"/><path d="M10 17l-7 8" stroke="var(--green)" stroke-width="3"/></svg>
      <h3 class="rule-title" style="margin-top:6px">5) Besichtigungen</h3>
      <div class="section">
        <p class="lead">Den passenden Käufer finden</p>
        <p class="body">Fingerspitzengefühl ist bei den Besichtigungen gefragt, denn in den wenigsten Fällen ist die Immobilie freistehend. Nicht nur die Kaufbereitschaft, sondern auch die Zusage der Bank ist bei der Vorauswahl der potentiellen Käufer wichtig.</p>
        <p class="body">Das Ergebnis der Vorauswahl besprechen wir gemeinsam.</p>
      </div>
      <div class="band">Neben den Fakten ist mir wichtig, dass sie<br>nachdem Verkauf sagen können „das passt“.</div>
    </div>
    <div style="position:absolute;top:720px;left:0;right:0">
      <svg class="icon" width="32" height="24" viewBox="0 0 32 24"><path d="M2 10l8-6 6 4 6-4 8 6-8 8-6-4-6 4z" fill="var(--green)"/></svg>
      <h3 class="rule-title" style="margin-top:6px">6) Kaufvertrag aushandeln</h3>
      <div class="section">
        <p class="lead">Übergabe begleiten</p>
        <p class="body">Zuhören, Lösungen finden, sich Zeit nehmen – der Ausarbeitung des Kaufvertrags gehört die meiste Sorgfalt.</p>
        <p class="body">Ich gebe Ihnen Antworten und zeige durch meine Erfahrung mit Notaren und auch Rechtsanwälten Möglichkeiten auf, um den Verkauf zu Ihrer vollsten Zufriedenheit abzuschließen.</p>
      </div>
      <div class="band">Nach der Schlüsselübergabe bin ich bei<br>Fragen weiterhin für Sie da.</div>
    </div>
  </section>
</div>

</body>
</html>
```